2009 Thank You

A colorful post card that is 8.5 x 5.5.  The purpose is to say thank you to our customers and to wish them a prosperous new year.  We a printing company and will print 4-color process on both sides of the post card

Requirements
Must have
• I have included our logo to be incorporated where appropriate 

Nice to have
• The theme might incorporate something that recognizes "these are turbulent times"  or "success from adversity"

```html
<!DOCTYPE html>
<html lang="en">
<head>
<meta charset="utf-8">
<title>Thank You Postcard 2009</title>
<link href="https://fonts.googleapis.com/css2?family=Pinyon+Script&display=swap" rel="stylesheet">
<style>
  :root {
    --ink: #000000;
    --gold: #ffee00;
    --amber: #ff9a1a;
    --orange: #ff7a00;
    --yellow: #ffff00;
    --script: "Pinyon Script", cursive;
  }
  html, body {
    margin: 0;
    padding: 0;
    width: 1200px;
    height: 776px;
    overflow: hidden;
    background: var(--ink);
  }
  .postcard {
    position: relative;
    width: 1200px;
    height: 776px;
    box-sizing: border-box;
    background: linear-gradient(135deg, var(--orange) 0%, var(--gold) 45%, var(--yellow) 100%);
    padding: 10px;
  }
  .postcard__panel {
    position: relative;
    width: 100%;
    height: 100%;
    background: var(--ink);
    overflow: hidden;
  }
  .headline {
    position: absolute;
    left: 0;
    top: 8px;
    width: 100%;
    margin: 0;
    font-family: var(--script);
    font-weight: 400;
    font-size: 176px;
    line-height: 1;
    text-align: center;
    letter-spacing: 2px;
    word-spacing: 40px;
    background: linear-gradient(90deg, var(--amber) 0%, #ffc400 45%, var(--yellow) 80%);
    -webkit-background-clip: text;
    background-clip: text;
    color: transparent;
  }
  .headline__rule {
    position: absolute;
    left: 35px;
    top: 207px;
    width: 1135px;
    height: 6px;
  }
  .message {
    position: absolute;
    left: 50px;
    right: 20px;
    top: 330px;
    margin: 0;
    font-family: var(--script);
    font-size: 31px;
    line-height: 42.5px;
    color: var(--yellow);
    text-align: center;
  }
  .message p { margin: 0 0 42px; }
  .message .signoff { margin-top: 0; }
</style>
</head>
<body>
  <main class="postcard">
    <div class="postcard__panel">
      <h1 class="headline">Thank You</h1>
      <svg class="headline__rule" viewBox="0 0 1135 6" aria-hidden="true">
        <defs>
          <linearGradient id="ruleGradient" x1="0" x2="1" y1="0" y2="0">
            <stop offset="0" stop-color="#ffa31a"/>
            <stop offset="1" stop-color="#ffff00"/>
          </linearGradient>
        </defs>
        <polygon points="0,0 1135,1 1130,5 5,4" fill="url(#ruleGradient)"/>
      </svg>
      <section class="message">
        <p>In these turbulent times it’s easy to forget that good things that are happening all around.<br>
        With this in mind, we just wanted to say thank you for your business in 2008.</p>
        <p>We hope you will enjoy a prosperous year in 2009.&nbsp;&nbsp; If there is anything we can do to help your company succeed, please give us a call.&nbsp; We are happy to provide printing services of all types including brochures, direct mail, multi-media campaigns to drive internet traffic, training materials and fulfillment services.</p>
        <p class="signoff">Give us a call!</p>
      </section>
    </div>
  </main>
</body>
</html>
```